Personal Training Studio Checkin App (or URL based)

I would like a simple web based app built for our  business. We have a training studio with a simple business model. All our clients buy sessions in packages either 4, 8, or 12 at a time. We want something that a trainer can pull up and Check in a client. This will record the date and time the client was checked in, by what trainer, and what type of session. This system will keep track of the following:
Whenever a Client Checks in so it will ‘tick off’ a session on their package (ie- they have gone from 11 sessions left to 10 sessions left)
Track what sessions a particular trainer does so we can pay them at the end of the week and look at who they trained, what type of session and how many
Look at client activity: Every time they check in, Recharge their package, any activity related to the client, even if it was admin – like deleting a session that was mistakenly recorded.
This will keep a database of clients added and all their activity
The pdf I have included lays out how I think it would work and the features I want
I would like this to run off an vornix that we have at our front check in counter. It can be an app or a URL that use.
***THIS PROJECT IS NOT SO MUCH ABOUT DESIGN BUT ABOUT FUNCTIONALITY OF THE APPLICATION. IT MUST HAVE THE FEATURES I HAVE ASKED FOR THAT WORK TOGETHER. I AM WILLING TO PAY A LITTLE MORE AS A BONUS IF YOU CAN ACCOMPLISH THIS. ALSO IF I FIN THE RIGHT PERSON THAT CAN DO THIS I WILL MAKE IT A GUARNTEED PROJECT.

- Functionality and Track and record all the info we need

```html
<!DOCTYPE html>
<html lang="en">
<head>
<meta charset="utf-8">
<title>The Forge – Register Now</title>
<link rel="stylesheet" href="https://fonts.googleapis.com/css2?family=Poppins:wght@400;500;600&display=swap">
<style>
:root{
  --orange:#ff4a00;
  --ink:#2b2b2b;
  --navy:#1d1f3c;
  --card:#eef0f4;
  --faq-bg:#f4f4f4;
  --footer:#262626;
  --muted:#8b8b8b;
  --field-border:#cfcfcf;
  --btn-grey:#565656;
  --scrim:rgba(0,0,0,.62);
}
*{margin:0;padding:0;box-sizing:border-box}
html,body{width:1200px;height:1178px;overflow:hidden}
body{font-family:'Poppins',sans-serif;color:var(--ink);background:#fff;position:relative}
.abs{position:absolute}

/* hero */
.hero{left:0;top:0;width:1200px;height:188px;background:linear-gradient(90deg,#1b2436 0%,#232a3d 45%,#3a1b1b 75%,#4a1712 100%)}
.slider-dots{left:1058px;top:168px;display:flex;gap:18px}
.slider-dots span{width:8px;height:8px;border-radius:50%;background:#fff}

/* header */
.nav-orange{left:334px;top:26px;width:416px;height:42px;background:var(--orange);clip-path:polygon(0 0,100% 0,97% 100%,0 100%)}
.nav-dark{left:740px;top:26px;width:460px;height:42px;background:#2b2b2b}
.brand{left:131px;top:16px;width:218px;height:61px}
.brand-name{left:172px;top:32px;font-size:22px;font-weight:600;color:#3a3a3a;letter-spacing:.5px}
.nav-link{top:26px;height:42px;display:flex;align-items:center;gap:7px;font-size:10.5px;color:#fff}
.nav-icon{width:21px;height:21px;border-radius:50%;background:#fff;display:flex;align-items:center;justify-content:center}
.site-link{top:26px;height:42px;display:flex;align-items:center;font-size:10px;color:#fff}
.call{left:934px;top:34px;display:flex;align-items:center;gap:6px;color:#fff}
.call-icon{width:24px;height:24px;border-radius:50%;background:var(--orange);display:flex;align-items:center;justify-content:center}
.call small{display:block;font-size:8px;line-height:1}
.call strong{display:block;font-size:11.5px;font-weight:600;line-height:1.3}

/* packages */
.packages{left:0;top:188px;width:1200px;height:212px;background:var(--navy)}
.pkg{top:300px;width:213px;height:100px;background:var(--card);padding:28px 18px;font-size:17.5px;font-weight:600;line-height:1.1;color:#333;overflow:hidden}
.pkg-num{position:absolute;right:16px;top:14px;font-size:60px;font-weight:600;color:rgba(0,0,0,.06)}
.pkg.active{background:var(--orange)}
.pkg.active .pkg-num{color:rgba(0,0,0,.12)}

/* detail */
.detail{left:0;top:400px;width:1200px;height:301px;background:#141414}
.detail-photo{left:600px;top:400px;width:600px;height:301px;background:linear-gradient(90deg,#141414 0%,#3b3f46 40%,#8c8077 75%,#6d6a6c 100%)}
.detail-title{left:156px;top:444px;font-size:20px;font-weight:600;color:var(--orange)}
.detail-sub{left:156px;top:470px;font-size:12.5px;color:#ddd}
.detail-text{left:156px;top:496px;width:384px;font-size:10.6px;line-height:16.5px;color:#bbb}
.detail-label{left:156px;top:566px;font-size:10px;color:#ccc}
.detail-select{left:156px;top:587px;width:206px;height:28px;border:1px solid #444;background:#1a1a1a;font-size:9.5px;color:#ccc;padding:6px 10px}
.detail-select::after{content:"";position:absolute;right:14px;top:12px;border:3px solid transparent;border-top-color:#ccc}
.detail-btn{left:156px;top:624px;width:121px;height:31px;background:#eee;font-size:12.5px;font-weight:500;display:flex;align-items:center;justify-content:center;color:#333}

/* faq */
.faq{left:0;top:701px;width:1200px;height:440px;background:var(--faq-bg)}
.faq-title{left:0;top:766px;width:1200px;text-align:center;font-size:25px;font-weight:600;color:#222}
.faq-list{left:264px;top:825px;width:673px;border-top:1px solid #ddd}
.faq-item{border-bottom:1px solid #ddd;position:relative;padding:14px 40px 14px 0;font-size:12px;font-weight:500}
.faq-item .toggle{position:absolute;right:7px;top:15px;width:16px;height:16px;border-radius:50%;background:#333}
.faq-item .toggle::before,.faq-item .toggle::after{content:"";position:absolute;left:4px;top:7.5px;width:8px;height:1.3px;background:#fff}
.faq-item .toggle::after{transform:rotate(90deg)}
.faq-item.open .q{color:var(--orange)}
.faq-item.open .toggle{background:var(--orange)}
.faq-item.open .toggle::after{display:none}
.faq-item .a{font-size:11.3px;font-weight:400;line-height:15px;margin-top:8px;color:#333;width:612px}

/* footer */
.footer{left:0;top:1141px;width:1200px;height:37px;background:var(--footer)}
.copyright{left:157px;top:1152px;font-size:11px;color:var(--muted)}
.social{top:1149px;width:21px;height:21px;display:flex;align-items:center;justify-content:center}
.social span{width:9px;height:9px;background:#aaa;border-radius:2px}
.social.hl{background:var(--orange);border-radius:50%;width:26px;height:26px;top:1147px}
.social.hl span{background:#fff}

/* modal */
.scrim{left:0;top:0;width:1200px;height:1178px;background:var(--scrim)}
.modal{left:434px;top:150px;width:332px;height:377px;background:#fff}
.modal-head{height:40px;background:var(--orange);display:flex;align-items:center;justify-content:space-between;padding:0 25px;color:#fff;font-size:15px;font-weight:600}
.modal-body{padding:20px 25px 0}
.field{margin-bottom:16px}
.field label{display:block;font-size:10px;line-height:12px;color:#444;margin-bottom:3px}
.field .input{height:31px;border:1px solid var(--field-border);padding:0 10px;display:flex;align-items:center;font-size:10px;color:#444}
.submit{width:83px;height:31px;background:var(--btn-grey);color:#fff;font-size:12.5px;font-weight:600;display:flex;align-items:center;justify-content:center}
</style>
</head>
<body>
<div class="abs hero" role="img" aria-label="Gym interior photograph with training equipment"></div>
<div class="abs slider-dots"><span></span><span></span><span></span><span></span></div>

<div class="abs nav-dark"></div>
<div class="abs nav-orange"></div>
<svg class="abs brand" viewBox="0 0 218 61"><polygon points="12,0 218,0 203,61 0,61" fill="#ff4a00"/><polygon points="17,0 218,0 205,58 4,58" fill="#e9e9ea"/></svg>
<div class="abs brand-name">The Forge</div>

<div class="abs nav-link" style="left:356px"><span class="nav-icon"><svg width="10" height="10" viewBox="0 0 10 10"><circle cx="5" cy="3.2" r="2" fill="#ff4a00"/><path d="M1 9.5c0-2.5 2-3.6 4-3.6s4 1.1 4 3.6z" fill="#ff4a00"/></svg></span>Client Check In</div>
<div class="abs nav-link" style="left:489px"><span class="nav-icon"><svg width="10" height="10" viewBox="0 0 10 10"><circle cx="4.5" cy="3.2" r="2" fill="#ff4a00"/><path d="M.5 9.5c0-2.5 2-3.6 4-3.6s4 1.1 4 3.6z" fill="#ff4a00"/></svg></span>Add New Client</div>
<div class="abs nav-link" style="left:626px"><span class="nav-icon"><svg width="10" height="10" viewBox="0 0 10 10"><rect x="1" y="1.5" width="8" height="7" fill="none" stroke="#ff4a00" stroke-width="1.2"/><rect x="3" y="4" width="4" height="2" fill="#ff4a00"/></svg></span>Admin Panel</div>
<div class="abs site-link" style="left:777px">Home</div>
<div class="abs site-link" style="left:830px">About</div>
<div class="abs site-link" style="left:884px">FAQs</div>
<div class="abs call"><span class="call-icon"><svg width="11" height="11" viewBox="0 0 12 12"><path d="M2.5 1l2 2.5-1 1.2a6 6 0 0 0 3.8 3.8l1.2-1 2.5 2-1.2 1.5C5 10.5 1.5 7 1 2.2z" fill="#fff"/></svg></span><span><small>Call Now</small><strong>555.014.2730</strong></span></div>

<div class="abs packages"></div>
<div class="abs pkg" style="left:156px">Single<br>Session<span class="pkg-num">1</span></div>
<div class="abs pkg" style="left:381px">Partner<br>Session<span class="pkg-num">2</span></div>
<div class="abs pkg active" style="left:606px">Partner<br>Only 1<span class="pkg-num">3</span></div>
<div class="abs pkg" style="left:831px">Drop In<br>Partner<span class="pkg-num">4</span></div>

<div class="abs detail"></div>
<div class="abs detail-photo" role="img" aria-label="Photograph of a smiling client in a gym"></div>
<div class="abs detail-title">Partner Session</div>
<div class="abs detail-sub">(Only 1 Party Showed)</div>
<p class="abs detail-text">Partner Session (Only 1 Partner Showed) This Is When Clients Have Bought A Partner Packaged, But Only 1 Person Showed That Day- It Is A Way For Us To Note The Trainer Only Trained One Person Not 2</p>
<div class="abs detail-label">Select Sessions To Buy:</div>
<div class="abs detail-select">4 Nos</div>
<div class="abs detail-btn">Register Now</div>

<div class="abs faq"></div>
<h2 class="abs faq-title">Frequently Asked Questions</h2>
<div class="abs faq-list">
  <div class="faq-item"><div class="q">What is Lorem Ipsum?</div><span class="toggle"></span></div>
  <div class="faq-item open"><div class="q">Why do we use it?</div><span class="toggle"></span>
    <p class="a">It is a long established fact that a reader will be distracted by the readable content of a page when looking at its layout. The point of using Lorem Ipsum is that it has a more-or-less normal distribution of letters, as opposed to using 'Content here, content here', making it look like readable English.</p></div>
  <div class="faq-item"><div class="q">How is this different from Promptly or other AI tools?</div><span class="toggle"></span></div>
  <div class="faq-item"><div class="q">What's the difference between joining the waitlist and becoming a Builder?</div><span class="toggle"></span></div>
</div>

<div class="abs footer"></div>
<div class="abs copyright">Copyright © 2025 The Forge Personal Training Studio. All rights reserved</div>
<div class="abs social" style="left:962px"><span></span></div>
<div class="abs social" style="left:991px"><span></span></div>
<div class="abs social hl" style="left:1018px"><span></span></div>

<div class="abs scrim"></div>
<div class="abs modal">
  <div class="modal-head">Register Now
    <svg width="14" height="14" viewBox="0 0 14 14"><circle cx="7" cy="7" r="6" fill="none" stroke="#fff" stroke-width="1.4"/><path d="M4.8 4.8l4.4 4.4M9.2 4.8l-4.4 4.4" stroke="#fff" stroke-width="1.4"/></svg>
  </div>
  <div class="modal-body">
    <div class="field"><label>First Name:</label><div class="input">Marla</div></div>
    <div class="field"><label>Last Name:</label><div class="input">Quinn</div></div>
    <div class="field"><label>Email Id:</label><div class="input">marla.quinn@mailbox.com</div></div>
    <div class="field"><label>Starting Package Session Amount:</label><div class="input">4 Nos</div></div>
    <div class="submit">Submit</div>
  </div>
</div>
</body>
</html>
```